Corona rapid test station

We need a banner for a container. This container will stand in the pedestrian zone of a large city. What is required is high-quality graphics with pictures of people who draw the eye, but also fit the topic of the Corona rapid test. One possible theme is the portrayal of young people getting tested to protect their older relatives.

Corona rapid test, result within 15 minutes
Pre-registration by phone: 0648/27 584 6

Leave empty field for price.

The umbrella brand should be clearly visible: Lindwurm-Apotheken (Attention, an n must be added to the existing logo: Lindwurm-Apotheken <-)

The branches are to be listed smaller: Lindwurm-Apotheke, Birk-Apotheke, Solveig-Apotheke, Tamara-Apotheke

Format: 2m high, 5.5m wide

Target Market(s)

People between 20 and 60 years of age

Requirements
Must have
• The logo of the umbrella brand Lindwurm-Apotheken stands above everything. The design of the central pharmacies (green / blue) is reflected in the overall design.
Font Nexa Bold or Nexa light
Nice to have
• Faces of people without a mask

```html
<!DOCTYPE html>
<html lang="en">
<head>
<meta charset="utf-8">
<title>Corona Rapid Test – Lindwurm-Apotheken</title>
<link rel="stylesheet" href="https://fonts.googleapis.com/css2?family=Montserrat:wght@300;600;800&display=swap">
<style>
  :root {
    --page-bg: #eceeef;
    --brand-green: #6fbf3f;
    --brand-blue: #1d4b8f;
    --white: #ffffff;
    --art-light: #dbe8f2;
    --art-mid: #9fb9cf;
  }
  * { margin: 0; padding: 0; box-sizing: border-box; }
  html, body {
    width: 1200px;
    height: 725px;
    overflow: hidden;
    background: var(--page-bg);
    font-family: "Montserrat", sans-serif;
  }
  .banner {
    position: absolute;
    left: 50px;
    top: 162px;
    width: 1100px;
    height: 400px;
    background: var(--brand-green);
    overflow: hidden;
    border-bottom: 10px solid var(--brand-blue);
  }
  .banner__wave {
    position: absolute;
    left: 0;
    bottom: 0;
    width: 1100px;
    height: 400px;
  }
  .banner__headline {
    position: absolute;
    left: 30px;
    top: 20px;
    color: var(--white);
    font-weight: 800;
    font-size: 58px;
    letter-spacing: 0.5px;
    line-height: 1;
    white-space: nowrap;
  }
  .banner__subline {
    position: absolute;
    left: 480px;
    top: 88px;
    color: var(--white);
    font-weight: 600;
    font-size: 24px;
    line-height: 1.1;
    white-space: nowrap;
  }
  .banner__phone {
    position: absolute;
    left: 480px;
    top: 120px;
    color: var(--white);
    font-weight: 600;
    font-size: 16px;
    line-height: 1.2;
    white-space: nowrap;
  }
  .banner__illustration {
    position: absolute;
    left: 0;
    top: 155px;
    width: 640px;
    height: 235px;
    background: linear-gradient(160deg, var(--art-light) 0%, var(--art-mid) 100%);
    border-top-right-radius: 170px 235px;
  }
  .brand {
    position: absolute;
    right: 30px;
    top: 26px;
    display: flex;
    align-items: center;
    gap: 10px;
    color: var(--white);
  }
  .brand__mark {
    width: 34px;
    height: 34px;
    border-radius: 50%;
    background: var(--white);
  }
  .brand__name {
    font-weight: 800;
    font-size: 24px;
    line-height: 1;
    white-space: nowrap;
  }
  .branches {
    position: absolute;
    right: 30px;
    top: 100px;
    display: flex;
    flex-direction: column;
    gap: 16px;
    list-style: none;
  }
  .branches__item {
    display: flex;
    align-items: center;
    gap: 8px;
    color: var(--white);
    font-weight: 600;
    font-size: 15px;
    line-height: 20px;
    white-space: nowrap;
  }
  .branches__badge {
    width: 20px;
    height: 20px;
    background: var(--white);
  }
  .price-field {
    position: absolute;
    right: 30px;
    bottom: 30px;
    width: 190px;
    height: 70px;
    border: 3px solid var(--white);
    border-radius: 6px;
  }
</style>
</head>
<body>
  <section class="banner">
    <svg class="banner__wave" viewBox="0 0 1100 400" aria-hidden="true">
      <path d="M0 330 C 250 400, 600 410, 900 300 L 1100 220 L 1100 400 L 0 400 Z" fill="var(--brand-blue)"/>
    </svg>
    <div class="banner__illustration" role="img" aria-label="Illustration: young person in front of a pharmacy with older relatives and floating virus particles"></div>
    <h1 class="banner__headline">CORONA RAPID TEST</h1>
    <p class="banner__subline">within 15 minutes</p>
    <p class="banner__phone">Pre-registration by phone 0648/27 584 6</p>
    <div class="brand">
      <span class="brand__mark"></span>
      <span class="brand__name">Lindwurm-Apotheken</span>
    </div>
    <ul class="branches">
      <li class="branches__item"><span class="branches__badge"></span>Lindwurm-Apotheke</li>
      <li class="branches__item"><span class="branches__badge"></span>Birk-Apotheke</li>
      <li class="branches__item"><span class="branches__badge"></span>Solveig-Apotheke</li>
      <li class="branches__item"><span class="branches__badge"></span>Tamara-Apotheke</li>
    </ul>
    <div class="price-field" aria-label="Price field"></div>
  </section>
</body>
</html>
```